Visitenkarten-Design für Handel mit Handstrickgarnen
Zielgruppe
Handel mit Handstrickgarnen, besonders Farbverläufe und handgefärbte Garne, aber auch Design von Strickmode. Die Zielgruppe sind alle, die gerne stricken oder häkeln, insbesondere Frauen aller Altersgruppen.
Aufgabenstellung
Schöne Farbverläufe bzw. Farbharmonien sind mir besonders wichtig und sollten insgesamt ins Auge stechen ohne jedoch zu grell bunt zu wirken. Sanft ineinander fließende Farben wären ideal, gerne auch etwas kräftigere Farben. Das Motiv des Logos könnte auch im Negativ sein auf dunklerem Hintergrund.

```html
<!DOCTYPE html>
<html lang="de">
<head>
<meta charset="utf-8">
<title>Farbwirbel – Visitenkarten</title>
<link rel="stylesheet" href="https://fonts.googleapis.com/css2?family=Cabin:wght@400;600&family=Montserrat:wght@700&display=swap">
<style>
  :root {
    --stage: #b9b9b9;
    --paper: #f6f6f4;
    --orange: #e2733a;
    --pink: #de4277;
    --magenta: #c94a82;
    --violet: #6a5796;
    --white: #ffffff;
    --band: rgba(255, 110, 140, 0.55);
  }
  * { box-sizing: border-box; margin: 0; padding: 0; }
  html, body { width: 1200px; height: 900px; overflow: hidden; }
  body {
    background: var(--stage);
    display: flex;
    align-items: center;
    justify-content: center;
    gap: 90px;
    font-family: "Cabin", sans-serif;
  }
  .card {
    width: 380px;
    height: 600px;
    position: relative;
    overflow: hidden;
    box-shadow: 0 12px 30px rgba(0,0,0,0.25);
  }

  /* Front: contact side */
  .card--front {
    background: linear-gradient(210deg, var(--orange) 0%, var(--pink) 45%, var(--magenta) 70%, var(--violet) 100%);
    color: var(--white);
  }
  .brand {
    position: absolute;
    top: 150px;
    left: 0;
    right: 0;
    display: flex;
    align-items: center;
    justify-content: center;
    gap: 14px;
  }
  .brand__dot {
    width: 34px;
    height: 34px;
    border-radius: 50%;
    background: var(--white);
  }
  .brand__name {
    font-family: "Cabin", sans-serif;
    font-weight: 600;
    font-size: 40px;
    letter-spacing: 1px;
    text-transform: uppercase;
  }
  .person {
    position: absolute;
    top: 300px;
    left: 0;
    right: 40px;
    padding: 18px 24px 18px 40px;
    background: linear-gradient(90deg, rgba(255,255,255,0.12), var(--band));
  }
  .person__name {
    font-family: "Montserrat", sans-serif;
    font-weight: 700;
    font-size: 24px;
  }
  .person__role { font-size: 19px; margin-top: 2px; }
  .contacts {
    position: absolute;
    top: 420px;
    left: 70px;
    list-style: none;
  }
  .contacts li {
    display: flex;
    align-items: center;
    gap: 16px;
    font-size: 20px;
    line-height: 1;
    margin-bottom: 14px;
  }
  .contacts svg { width: 20px; height: 20px; fill: var(--white); flex: none; }

  /* Back: brand side */
  .card--back { background: var(--paper); }
  .back__band {
    position: absolute;
    left: 0; top: 0; bottom: 0;
    width: 64px;
    background: linear-gradient(180deg, var(--violet) 0%, var(--pink) 50%, var(--orange) 100%);
  }
  .back__url {
    position: absolute;
    left: 32px;
    top: 50%;
    transform: translate(-50%, -50%) rotate(90deg);
    color: var(--white);
    font-size: 16px;
    white-space: nowrap;
  }
  .back__brand {
    position: absolute;
    left: 64px; right: 0; top: 0; bottom: 0;
    display: flex;
    align-items: center;
    justify-content: center;
    gap: 12px;
  }
  .back__brand .brand__dot { background: var(--pink); width: 30px; height: 30px; }
  .back__brand .brand__name { color: var(--pink); font-size: 38px; }
</style>
</head>
<body>
  <article class="card card--front">
    <div class="brand">
      <span class="brand__dot"></span>
      <span class="brand__name">Farbwirbel</span>
    </div>
    <div class="person">
      <p class="person__name">Lena Wollmann</p>
      <p class="person__role">Geschäftsführerin</p>
    </div>
    <ul class="contacts">
      <li>
        <svg viewBox="0 0 24 24" aria-hidden="true"><path d="M6.6 10.8a15 15 0 0 0 6.6 6.6l2.2-2.2a1 1 0 0 1 1-.25 11.4 11.4 0 0 0 3.6.6 1 1 0 0 1 1 1V20a1 1 0 0 1-1 1A17 17 0 0 1 3 4a1 1 0 0 1 1-1h3.5a1 1 0 0 1 1 1c0 1.25.2 2.45.6 3.6a1 1 0 0 1-.25 1z"/></svg>
        0987/ 4321 00
      </li>
      <li>
        <svg viewBox="0 0 24 24" aria-hidden="true"><path d="M7 3h10v5H7zM4 9h16a2 2 0 0 1 2 2v6h-4v4H6v-4H2v-6a2 2 0 0 1 2-2zm4 7v3h8v-3z"/></svg>
        0987/ 4321 01
      </li>
      <li>
        <svg viewBox="0 0 24 24" aria-hidden="true"><path d="M2 5h20v14H2zm2 2v.5l8 5 8-5V7l-8 5z"/></svg>
        hallo@farbwirbel.de
      </li>
      <li>
        <svg viewBox="0 0 24 24" aria-hidden="true"><path d="M12 2a10 10 0 1 0 0 20 10 10 0 0 0 0-20zm-1 17.9A8 8 0 0 1 4.1 11H7c.1 3 1.5 6.4 4 8.9zM4.1 9A8 8 0 0 1 11 4.1C8.5 6.6 7.1 9 7 9zm5 2h5.8c-.1 2.6-1.1 5.3-2.9 7.3-1.8-2-2.8-4.7-2.9-7.3zm0-2c.1-2 1.1-4.2 2.9-6 1.8 1.8 2.8 4 2.9 6zM13 19.9c2.5-2.5 3.9-5.9 4-8.9h2.9A8 8 0 0 1 13 19.9zM17 9c-.1 0-1.5-2.4-4-4.9A8 8 0 0 1 19.9 9z"/></svg>
        farbwirbel.de/kontakt
      </li>
    </ul>
  </article>

  <article class="card card--back">
    <div class="back__band">
      <span class="back__url">www.farbwirbel.de</span>
    </div>
    <div class="back__brand">
      <span class="brand__dot"></span>
      <span class="brand__name">Farbwirbel</span>
    </div>
  </article>
</body>
</html>
```